Product Insert / Thank You

I'm looking for a small card to be designed that will be included with our product when it ships. It will be 2 sided with 1 side being a "thank you" with our logo and the other side containing the following text:We would love to hear your feedback! For every review we receive on our products, we donate 100% of the proceeds of your order to TIDEWELL -- a non profit organization dedicated to preserving our oceans!If you are not 100% satisfied with your purchase or have any problems, we will always resolve your issue. please contact us via Brisko if you need assistance.Insert needs to be well organized and information presented in a clear and visually appealing way.
Target Market(s)
Women, aged 24-45
Colors
Designer to choose colors to be used in the design.
Look and feel
Each slider illustrates characteristics of the customer's brand and the style your logo design should communicate.

```html
<!DOCTYPE html>
<html lang="en">
<head>
<meta charset="utf-8">
<title>Northmere Thank You Insert</title>
<link rel="stylesheet" href="https://fonts.googleapis.com/css2?family=Roboto+Condensed:ital,wght@0,400;0,700;1,400&display=swap">
<style>
  :root {
    --stage: #2b2c2f;
    --ink: #0b0b0b;
    --paper: #ffffff;
    --text: #161616;
  }
  * { box-sizing: border-box; margin: 0; padding: 0; }
  html, body { width: 1200px; height: 900px; overflow: hidden; }
  body {
    background: var(--stage);
    font-family: "Roboto Condensed", "Arial Narrow", sans-serif;
    position: relative;
  }
  .card {
    position: absolute;
    width: 640px;
    height: 366px;
    background: var(--ink);
    overflow: hidden;
  }
  .card-back { left: 280px; top: 60px; }
  .card-front { left: 280px; top: 474px; }

  /* Back side */
  .back-band {
    position: absolute;
    left: 0; right: 0; top: 30px; height: 306px;
    background: var(--paper);
  }
  .back-rule {
    position: absolute;
    height: 4px;
    background: var(--ink);
  }
  .rule-top-left { left: 0; top: 40px; width: 240px; }
  .rule-top-right { right: 0; top: 40px; width: 240px; }
  .rule-bottom { left: 0; right: 0; bottom: 14px; }
  .rule-side-left { left: 40px; top: 300px; width: 110px; height: 3px; }
  .rule-side-right { right: 40px; top: 300px; width: 110px; height: 3px; }

  .brand-badge {
    position: absolute;
    left: 50%; top: 16px;
    width: 140px; height: 140px;
    margin-left: -70px;
    border-radius: 50%;
    background: var(--paper);
    border: 6px solid var(--ink);
    display: flex; align-items: center; justify-content: center;
  }
  .brand-name {
    font-weight: 700;
    font-size: 20px;
    letter-spacing: 1px;
    color: var(--ink);
    white-space: nowrap;
  }

  .message {
    position: absolute;
    left: 40px; right: 40px; top: 166px;
    text-align: center;
    color: var(--text);
    font-size: 15px;
    line-height: 1.3;
  }
  .message .lead { font-weight: 700; }
  .message strong { font-weight: 700; }
  .message .help { font-style: italic; font-size: 14px; margin-top: 2px; }

  /* Front side */
  .front-stripe {
    position: absolute;
    left: 0; right: 0;
    height: 12px;
    background: var(--paper);
  }
  .stripe-one { top: 156px; }
  .stripe-two { top: 184px; }
  .thanks-badge {
    position: absolute;
    left: 50%; top: 50%;
    width: 250px; height: 250px;
    margin: -125px 0 0 -125px;
    border-radius: 50%;
    background: var(--paper);
    border: 9px solid var(--ink);
    box-shadow: 0 0 0 8px var(--paper);
    display: flex; align-items: center; justify-content: center;
  }
  .thanks-text {
    font-weight: 700;
    font-size: 36px;
    letter-spacing: 1px;
    color: var(--ink);
    white-space: nowrap;
  }
</style>
</head>
<body>

  <section class="card card-back" aria-label="Insert back">
    <div class="back-band">
      <span class="back-rule rule-top-left"></span>
      <span class="back-rule rule-top-right"></span>
      <span class="back-rule rule-bottom"></span>
    </div>
    <span class="back-rule rule-side-left"></span>
    <span class="back-rule rule-side-right"></span>
    <div class="brand-badge"><span class="brand-name">NORTHMERE</span></div>
    <div class="message">
      <p class="lead">We would love to hear your feedback!</p>
      <p>For every review we receive on our products, we donate <strong>100%</strong> of the proceeds of your<br>order to <strong>TIDEWELL</strong> – a non profit organization dedicated to preserving our oceans!</p>
      <p>If you are not <strong>100%</strong> satisfied with your purchase or have any problems,<br>we will always resolve your issue.</p>
      <p class="help">Please Contact Us Via Brisko If You Need Assistance.</p>
    </div>
  </section>

  <section class="card card-front" aria-label="Insert front">
    <span class="front-stripe stripe-one"></span>
    <span class="front-stripe stripe-two"></span>
    <div class="thanks-badge"><span class="thanks-text">THANK YOU</span></div>
  </section>

</body>
</html>
```